new TRV one page flyer

We need a 1 page A4 size flyer (need it asap please) that describes on 1 page with art work and using photos the services we provide. I have included some examples of old previous flyers from our other (seperate divisions of the business) I have named a photo called (photo for top of design) however you do your design this photo needs to be the star of the page by either having it at the top or bottom of the page please and we usually like this photo to be in greyscale colour.
we do like greyscale designs but are open to see what you come up with as a whole page of grey white and black might not suit.

Needs to list the following

Services include:
Over size loads / Hot Shot Loads
Heavy Vehicle Recovery services
Potable Water Deliveries
Road Building / Maintenance
Earthworks
Sand & Metal Supply & Cartage
Road Train Tippers
Road Train Tankers
Road Train Flat Tops
Drop Deck Trailers
Mine site accredited equipment & Operators.

We offer a large rage of services not listed so call us today for a personalised quote to suit your needs.

To go on the bottom of the page our contact details are

TRV Pty Ltd
Depot: Lot 519, Bramwell Creek Track Ridgeway Flat
Mobile: 047 312 6958
email: darren@tanrivervehicles.com.au

give extra time for designers to work on design

Target Market(s)

new clients

Colors

Designer to choose colors to be used in the design.

Requirements
Must have
• our services listed
Nice to have
• stand out designs

```html
<!DOCTYPE html>
<html lang="en">
<head>
<meta charset="utf-8">
<title>TRV Pty Ltd – Services Flyer</title>
<link rel="stylesheet" href="https://fonts.googleapis.com/css2?family=Russo+One&family=Montserrat:wght@400;500&family=Tinos&display=swap">
<style>
  :root {
    --sky-blue: #1ea0dc;
    --deep-blue: #1479ad;
    --band-blue: #1a7fae;
    --arrow-blue: #5cc3ea;
    --ink: #2b2b2b;
    --silver: #d9dde0;
    --white: #ffffff;
  }
  * { margin: 0; padding: 0; box-sizing: border-box; }
  html, body { width: 854px; height: 1200px; overflow: hidden; background: var(--white); }
  .flyer { position: relative; width: 854px; height: 1200px; overflow: hidden;
    background: radial-gradient(ellipse at 75% 62%, #ffffff 0%, #eef1f3 55%, #dde2e6 100%); }

  .hero-photo { position: absolute; left: 0; top: 0; width: 854px; height: 560px;
    background: linear-gradient(180deg, #4a4d50 0%, #5d6063 38%, #6b5a4c 62%, #5a4a3e 100%); }
  .shapes { position: absolute; left: 0; top: 0; }

  .brand-name { position: absolute; top: 58px; width: 100%; text-align: center;
    font-family: "Russo One", sans-serif; font-size: 58px; color: var(--silver); letter-spacing: 4px; }

  .call-line { position: absolute; width: 100%; text-align: center; font-family: "Russo One", sans-serif;
    color: var(--silver); text-shadow: 2px 2px 2px rgba(0,0,0,.55); }
  .call-line .label { font-size: 24px; letter-spacing: 1px; margin-right: 18px; }
  .call-line .number { font-size: 40px; letter-spacing: 2px; }
  .call-top { top: 130px; }

  .services { position: absolute; left: 48px; top: 574px; font-family: "Montserrat", sans-serif; }
  .services h2 { font-weight: 400; font-size: 21px; color: var(--sky-blue); margin-bottom: 6px; }
  .services ul { list-style: none; }
  .services li { display: flex; align-items: center; height: 27.6px; font-size: 16.5px; color: var(--ink); }
  .services li svg { margin: 0 10px 0 6px; flex: none; }

  .photo-bubble { position: absolute; border-radius: 50%; border: 7px solid var(--white);
    box-shadow: 0 4px 14px rgba(0,0,0,.25);
    background: linear-gradient(180deg, #6fb4e6 0%, #a9d3ef 45%, #b8865a 62%, #9a6a44 100%); }

  .cta-band { position: absolute; left: 0; top: 918px; width: 854px; height: 176px; background: var(--band-blue); }
  .cta-band .not-listed { position: absolute; top: 26px; width: 100%; text-align: center;
    font-family: "Russo One", sans-serif; font-size: 25px; color: var(--silver); letter-spacing: 2px;
    text-shadow: 2px 2px 2px rgba(0,0,0,.45); }
  .cta-band .call-line { top: 66px; }
  .cta-band .quote { position: absolute; top: 124px; width: 100%; text-align: center;
    font-family: "Russo One", sans-serif; font-size: 21px; color: var(--white); letter-spacing: 4px; }

  .footer { position: absolute; left: 0; top: 1094px; width: 854px; height: 106px; background: var(--white);
    font-family: "Tinos", serif; font-size: 13.5px; color: #111; text-transform: uppercase; }
  .footer-triangle { position: absolute; left: 0; top: 0; }
  .footer .depot { position: absolute; left: 40px; top: 34px; line-height: 26px; }
  .footer .contact { position: absolute; right: 40px; top: 34px; line-height: 26px; text-align: right; }
  .footer-brand { position: absolute; left: 0; width: 100%; top: 50px; text-align: center;
    font-family: "Russo One", sans-serif; font-size: 22px; color: var(--white); text-transform: none; }
</style>
</head>
<body>
<main class="flyer">
  <div class="hero-photo" role="img" aria-label="Greyscale photo of a road train with three side-tipper trailers on an outback dirt track"></div>

  <svg class="shapes" width="854" height="1200" viewBox="0 0 854 1200" aria-hidden="true">
    <polygon points="854,180 854,470 430,482" fill="var(--sky-blue)"/>
    <polygon points="854,470 430,482 854,560" fill="var(--deep-blue)"/>
    <polygon points="0,432 432,480 0,566" fill="var(--sky-blue)"/>
    <polygon points="0,540 432,480 854,560 854,570 0,570" fill="#eef1f3"/>
    <polygon points="0,432 432,480 0,470" fill="var(--deep-blue)" opacity=".6"/>
  </svg>

  <div class="brand-name">TRV</div>
  <div class="call-line call-top"><span class="label">CALL US TODAY</span><span class="number">4731 260 958</span></div>

  <section class="services">
    <h2>We offer a large rage of services</h2>
    <ul>
      <li><svg width="18" height="12" viewBox="0 0 18 12"><path d="M0 4h10V0l8 6-8 6V8H0z" fill="var(--arrow-blue)"/></svg>Over size loads / Hot Shot Loads</li>
      <li><svg width="18" height="12" viewBox="0 0 18 12"><path d="M0 4h10V0l8 6-8 6V8H0z" fill="var(--arrow-blue)"/></svg>Heavy Vehicle Recovery services</li>
      <li><svg width="18" height="12" viewBox="0 0 18 12"><path d="M0 4h10V0l8 6-8 6V8H0z" fill="var(--arrow-blue)"/></svg>Potable Water Deliveries</li>
      <li><svg width="18" height="12" viewBox="0 0 18 12"><path d="M0 4h10V0l8 6-8 6V8H0z" fill="var(--arrow-blue)"/></svg>Road Building / Maintenance</li>
      <li><svg width="18" height="12" viewBox="0 0 18 12"><path d="M0 4h10V0l8 6-8 6V8H0z" fill="var(--arrow-blue)"/></svg>Earthworks</li>
      <li><svg width="18" height="12" viewBox="0 0 18 12"><path d="M0 4h10V0l8 6-8 6V8H0z" fill="var(--arrow-blue)"/></svg>Sand &amp; Metal Supply &amp; Cartage</li>
      <li><svg width="18" height="12" viewBox="0 0 18 12"><path d="M0 4h10V0l8 6-8 6V8H0z" fill="var(--arrow-blue)"/></svg>Road Train Tippers</li>
      <li><svg width="18" height="12" viewBox="0 0 18 12"><path d="M0 4h10V0l8 6-8 6V8H0z" fill="var(--arrow-blue)"/></svg>Road Train Tankers</li>
      <li><svg width="18" height="12" viewBox="0 0 18 12"><path d="M0 4h10V0l8 6-8 6V8H0z" fill="var(--arrow-blue)"/></svg>Road Train Flat Tops</li>
      <li><svg width="18" height="12" viewBox="0 0 18 12"><path d="M0 4h10V0l8 6-8 6V8H0z" fill="var(--arrow-blue)"/></svg>Drop Deck Trailers</li>
      <li><svg width="18" height="12" viewBox="0 0 18 12"><path d="M0 4h10V0l8 6-8 6V8H0z" fill="var(--arrow-blue)"/></svg>Mine site accredited equipment &amp; Operators.</li>
    </ul>
  </section>

  <div class="photo-bubble" style="left:427px;top:567px;width:150px;height:150px" role="img" aria-label="Photo of graders and earthmoving machinery on red dirt"></div>
  <div class="photo-bubble" style="left:592px;top:514px;width:124px;height:124px" role="img" aria-label="Photo of the depot shed with trucks parked out front"></div>
  <div class="photo-bubble" style="left:717px;top:533px;width:134px;height:134px" role="img" aria-label="Photo of a prime mover hauling a water tanker"></div>
  <div class="photo-bubble" style="left:570px;top:640px;width:190px;height:190px" role="img" aria-label="Photo of two prime movers parked side by side"></div>
  <div class="photo-bubble" style="left:405px;top:695px;width:150px;height:150px" role="img" aria-label="Photo of a truck carrying a transportable site building"></div>
  <div class="photo-bubble" style="left:525px;top:760px;width:160px;height:150px" role="img" aria-label="Photo of a road train pulling a line of tanker trailers"></div>

  <section class="cta-band">
    <div class="not-listed">NOT LISTED ?</div>
    <div class="call-line"><span class="label">CALL US TODAY</span><span class="number">4731 260 958</span></div>
    <div class="quote">GET PERSONALISED QUOTE TO SUIT YOUR NEEDS.</div>
  </section>

  <footer class="footer">
    <svg class="footer-triangle" width="854" height="106" viewBox="0 0 854 106" aria-hidden="true">
      <polygon points="408,0 488,106 328,106" fill="var(--sky-blue)"/>
    </svg>
    <div class="depot">TRV Pty Ltd Depot: Lot 519<br>Bramwell Creek Track Ridgeway Flat</div>
    <div class="footer-brand">TRV</div>
    <div class="contact">Mobile: 047 312 6958<br>Email: darren@tanrivervehicles.com.au</div>
  </footer>
</main>
</body>
</html>
```